Brivolt: Electrical Contractor flyer design.

We are looking for a sharp and professional flyer to promote the business's cost for specific jobs and to promote the business.
We are a small electrical business looking to break into the market.
Attached logo to be used and following content to be incorporated. Contact details will be given upon final flyer design.

Internal Power Points: $ 120
External Weather Proof Power Points: $150
T.V. Points: $120 (excludes aerial)
T.V. Mounting: $ 200 (Exclude Leads)
Aerials Starting From: $220 Incudes Mast
LED Down lights: $60 per unti
Ceiling Fans: $150 (Fan Excluded)
Oven & Range Hood Change Overs: $250
A.C. Install: $300
S/B Upgrade: From $600
Safety Switch Installation: $280
Phone Points: $120

Services Incude:

New home wiring
Shop & Office Fit Outs
Re - Wires
Extentions
Garden Lighting
Home Thearters
Home Automation
Power Points
Phone, Data
Feature Lighting
Lighting design and Installation
Ceiling Fans
A.C Installation
Oven & Range hood Installation

*All prices are gst inclusive
**Prices subject to change due to site access.

```html
<!DOCTYPE html>
<html lang="en">
<head>
<meta charset="utf-8">
<title>Brivolt – Electrical Contractor Flyer</title>
<link rel="stylesheet" href="https://fonts.googleapis.com/css2?family=Russo+One&family=Roboto:ital,wght@0,400;0,500;0,700;1,400;1,500;1,700&display=swap">
<style>
  :root {
    --backdrop: #d4d5d7;
    --paper: #ffffff;
    --orange: #e8671e;
    --ink: #3f3f3f;
    --ink-soft: #555555;
    --rule: #4a4a4a;
  }
  * { margin: 0; padding: 0; box-sizing: border-box; }
  html, body { width: 1200px; height: 960px; overflow: hidden; }
  body {
    background: var(--backdrop);
    font-family: "Roboto", Arial, sans-serif;
    color: var(--ink);
    position: relative;
  }
  .page {
    position: absolute;
    top: 90px;
    width: 550px;
    height: 780px;
    background: var(--paper);
    overflow: hidden;
    box-shadow: 2px 4px 8px rgba(0,0,0,0.25);
  }
  .page--prices { left: 46px; }
  .page--services { left: 621px; }

  .hero { position: absolute; left: 0; top: 0; width: 550px; }
  .hero--bulbs {
    height: 296px;
    background:
      radial-gradient(circle at 60px 160px, #fff8d8 0, #ffd23a 40px, rgba(250,170,30,0.6) 110px, rgba(240,130,20,0) 220px),
      linear-gradient(180deg, #f28a1c 0%, #e5761a 60%, #c65a14 100%);
  }
  .hero--cables {
    height: 291px;
    background: radial-gradient(ellipse at 50% 45%, #fde2d2 0, #f9b595 25%, #f08656 55%, #e8683a 100%);
  }
  .tab { position: absolute; left: 0; width: 550px; }

  .display {
    font-family: "Russo One", "Arial Black", sans-serif;
    text-transform: uppercase;
    transform: skewX(-14deg);
    text-align: center;
    position: absolute;
    left: 0; width: 550px;
    line-height: 1;
    white-space: nowrap;
  }
  .headline { color: var(--ink); font-size: 25px; letter-spacing: 3px; }
  .headline--1 { top: 264px; }
  .headline--2 { top: 295px; }
  .tagline-rule { position: absolute; left: 45px; width: 461px; height: 1px; background: var(--rule); }
  .tagline {
    color: var(--orange);
    font-size: 34px;
    top: 333px;
    left: 45px; width: 461px;
    letter-spacing: 3px;
  }

  .price-list {
    position: absolute;
    top: 393px;
    left: 0; width: 550px;
    list-style: none;
    text-align: center;
    font-size: 15.5px;
    line-height: 21px;
  }
  .price-list .job { font-weight: 500; color: var(--ink); }
  .price-list .cost { color: var(--orange); font-weight: 400; }

  .footer-band { position: absolute; left: 0; top: 663px; width: 550px; height: 117px; }
  .brand {
    position: absolute;
    top: 690px;
    left: 0; width: 550px;
    display: flex;
    justify-content: center;
    align-items: center;
    gap: 10px;
    font-weight: 700;
    font-size: 42px;
    color: var(--ink);
    letter-spacing: 0.5px;
  }
  .brand-mark { width: 26px; height: 26px; background: var(--orange); }

  .section-title { color: var(--ink); font-size: 18px; top: 281px; letter-spacing: 2px; }
  .service-list {
    position: absolute;
    top: 328px;
    list-style: none;
    font-size: 15.5px;
    font-weight: 500;
    line-height: 21px;
    color: var(--ink);
  }
  .service-list--a { left: 42px; }
  .service-list--b { left: 256px; }
  .service-list li { display: flex; align-items: center; gap: 5px; }
  .service-list li::before { content: ""; width: 11px; height: 11px; background: var(--orange); flex: none; }
  .note-rule { position: absolute; left: 47px; width: 456px; height: 1px; background: var(--rule); }
  .notes {
    position: absolute;
    top: 499px;
    left: 0; width: 550px;
    text-align: center;
    font-style: italic;
    font-size: 13px;
    line-height: 21px;
    color: var(--ink-soft);
  }
  .contact-title { color: var(--ink); font-size: 13px; top: 559px; letter-spacing: 2px; }
  .contact {
    position: absolute;
    top: 582px;
    left: 0; width: 550px;
    text-align: center;
    font-style: italic;
    font-weight: 500;
    font-size: 15.5px;
    line-height: 18.5px;
    color: var(--orange);
    list-style: none;
  }
</style>
</head>
<body>

<section class="page page--prices">
  <div class="hero hero--bulbs" role="img" aria-label="Row of hanging light bulbs on an orange background, the first bulb glowing"></div>
  <svg class="tab" style="top:240px" width="550" height="60" viewBox="0 0 550 60" aria-hidden="true">
    <path d="M0 56 H106 L114 16 Q117 4 130 4 H438 Q450 4 450 16 V30 L442 56 H550 V60 H0 Z" fill="#ffffff"/>
  </svg>
  <div class="display headline headline--1">Electricity</div>
  <div class="display headline headline--2">In Motion</div>
  <div class="tagline-rule" style="top:332px"></div>
  <div class="display tagline">At Best Prices</div>
  <div class="tagline-rule" style="top:367px"></div>

  <ul class="price-list">
    <li><span class="job">Internal Power Points:</span> <span class="cost">$120</span></li>
    <li><span class="job">External Weather Proof Power Points:</span> <span class="cost">$150</span></li>
    <li><span class="job">T.V. Points:</span> <span class="cost">$120 (excludes aerial)</span></li>
    <li><span class="job">T.V. Mounting:</span> <span class="cost">$200 (Exclude Leads)</span></li>
    <li><span class="job">Aerials Starting From:</span> <span class="cost">$220 Incudes Mast</span></li>
    <li><span class="job">LED Down lights:</span> <span class="cost">$60 per unti</span></li>
    <li><span class="job">Ceiling Fans:</span> <span class="cost">$150 (Fan Excluded)</span></li>
    <li><span class="job">Oven &amp; Range Hood Change Overs:</span> <span class="cost">$250</span></li>
    <li><span class="job">A.C. Install:</span> <span class="cost">$300</span></li>
    <li><span class="job">S/B Upgrade:</span> <span class="cost">from $600</span></li>
    <li><span class="job">Safety Switch Installation:</span> <span class="cost">$280</span></li>
    <li><span class="job">Phone Points:</span> <span class="cost">$120</span></li>
  </ul>

  <svg class="footer-band" width="550" height="117" viewBox="0 0 550 117" aria-hidden="true">
    <defs>
      <linearGradient id="bandA" x1="0" y1="0" x2="1" y2="0">
        <stop offset="0" stop-color="#e25f1c"/><stop offset="1" stop-color="#ee7a20"/>
      </linearGradient>
    </defs>
    <path d="M0 0 H114 L86 117 H0 Z" fill="url(#bandA)"/>
    <path d="M448 0 H550 V117 H421 Z" fill="url(#bandA)"/>
  </svg>
  <div class="brand"><span class="brand-mark"></span>Brivolt</div>
</section>

<section class="page page--services">
  <div class="hero hero--cables" role="img" aria-label="Stripped blue, orange and green-yellow electrical cables on a soft orange background"></div>
  <svg class="tab" style="top:264px" width="550" height="30" viewBox="0 0 550 30" aria-hidden="true">
    <path d="M0 27 H107 L112 12 Q115 4 126 4 H436 Q446 4 446 14 V27 H550 V30 H0 Z" fill="#ffffff"/>
  </svg>
  <div class="display section-title">Services Include:</div>

  <ul class="service-list service-list--a">
    <li>New home wiring</li>
    <li>Shop &amp; Office Fit Outs</li>
    <li>Re - Wires</li>
    <li>Extentions</li>
    <li>Garden Lighting</li>
    <li>Home Thearters</li>
    <li>Home Automation</li>
  </ul>
  <ul class="service-list service-list--b">
    <li>Power Points</li>
    <li>Phone, Data</li>
    <li>Feature Lighting</li>
    <li>Lighting design and Installation</li>
    <li>Ceiling Fans</li>
    <li>A.C Installation</li>
    <li>Oven &amp; Range hood Installation</li>
  </ul>

  <div class="note-rule" style="top:495px"></div>
  <div class="notes">
    <p>*All prices are gst inclusive</p>
    <p>**Prices subject to change due to site access</p>
  </div>
  <div class="note-rule" style="top:543px"></div>

  <div class="display contact-title">Contact Us</div>
  <ul class="contact">
    <li>office@brivolt.com</li>
    <li>+1 555 01 234 56</li>
    <li>www.brivolt.com | Chatterly page</li>
  </ul>

  <svg class="footer-band" width="550" height="117" viewBox="0 0 550 117" aria-hidden="true">
    <defs>
      <linearGradient id="bandB" x1="0" y1="0" x2="1" y2="0">
        <stop offset="0" stop-color="#e25f1c"/><stop offset="1" stop-color="#ee7a20"/>
      </linearGradient>
    </defs>
    <path d="M0 0 H114 L86 117 H0 Z" fill="url(#bandB)"/>
    <path d="M448 0 H550 V117 H421 Z" fill="url(#bandB)"/>
  </svg>
  <div class="brand"><span class="brand-mark"></span>Brivolt</div>
</section>

</body>
</html>
```